Seed Oil Safety Card for Healthy Restaurant Dining

I am seeking a design for a physical card to communicate my wife's health-related dietary restriction regarding seed oils. This card will be given to restaurant waiters to ensure her meals are prepared without seed oils, as it is a health issue and not merely a preference.
My wife cannot eat any “seed oil” or “processed oil”, including:
- Vegetable oil
- Canola oil
- Soybean oil
- Sunflower oil
- Corn oil
- Cottonseed oil
- Safflower oil
- Peanut oil
- Sesame oil
Oils that are OK for her to consume:
- Butter (most preferable)
- Extra virgin olive oil
- Avocado oil
- Coconut oil
- Ghee
- Lard
- Any other animal-based fats
Key Design Requirements:
- Clarity and speed of communication: The card should be easily read and understood by waiters, even in low-light environments, emphasizing that it's a health concern.
- Avoid common misconceptions: Ensure the design doesn't imply common dietary preferences like "vegetarian" or "no butter." Animal fats and butter are actually preferable for her!
- Preferred term: Use "seed oils" as the term to describe what she cannot eat due to her health issue.
- Trace amounts are acceptable: Communicate that it's OK to use cookware that has previously been in contact with seed oils, but not to have seed oil as an ingredient. Please suggest a concise way to convey this.
- Card dimensions: Design should be 3.5” x 2.25” (standard credit-card size on cardlomex.example). Horizontal or vertical layouts are both fine, whichever makes the message clearer.
Design Suggestions:
- Utilize bold and easy-to-read typography to communicate the main message.
- Consider incorporating relevant icons or graphics that help convey the message without adding confusion.
- Use contrasting colors to enhance readability, especially in low-light situations.
- To communicate the “trace amounts OK” part, consider phrases such as:
- "Cross-contamination acceptable"
- “Used cookware OK, no ingredient use”
- “Separate cookware not necessary”
Thank you for your assistance in creating this essential card for my wife's health and safety when dining out!

```html
<!DOCTYPE html>
<html lang="en">
<head>
<meta charset="utf-8">
<title>Medical Dietary Restriction Card</title>
<link href="https://fonts.googleapis.com/css2?family=Lato:ital,wght@0,400;0,700;0,900;1,400&display=swap" rel="stylesheet">
<style>
  :root {
    --page-bg: #dfe0e2;
    --brand-blue: #1170b5;
    --deny-red: #c8202f;
    --allow-green: #2e8a35;
    --ink: #1f2328;
    --card-white: #ffffff;
    --card-mist: #e6e9ee;
  }
  html, body {
    margin: 0;
    padding: 0;
    width: 1200px;
    height: 2743px;
    overflow: hidden;
    background: var(--page-bg);
    font-family: "Lato", sans-serif;
  }
  .card {
    position: absolute;
    left: 100px;
    top: 1051px;
    width: 1000px;
    height: 640px;
    border-radius: 40px;
    overflow: hidden;
    background:
      radial-gradient(ellipse 60% 30% at 30% 75%, rgba(214,219,227,.7), transparent 70%),
      radial-gradient(ellipse 50% 40% at 80% 55%, rgba(220,224,231,.8), transparent 70%),
      linear-gradient(160deg, var(--card-white) 30%, var(--card-mist) 100%);
  }
  .card svg.bands { position: absolute; left: 0; top: 0; }
  .emblem-area {
    position: absolute;
    left: 694px;
    top: 0;
    width: 306px;
    height: 250px;
    background: radial-gradient(ellipse at 50% 40%, rgba(200,205,212,.75), rgba(220,224,230,0) 70%);
  }
  .title-kicker {
    position: absolute;
    left: 48px;
    top: 32px;
    margin: 0;
    color: var(--card-white);
    font-size: 36px;
    font-weight: 400;
    letter-spacing: 7px;
  }
  .title-main {
    position: absolute;
    left: 46px;
    top: 72px;
    margin: 0;
    color: var(--card-white);
    font-size: 48px;
    font-weight: 900;
    letter-spacing: -0.5px;
  }
  .status-icon { position: absolute; width: 66px; height: 66px; }
  .col-heading {
    position: absolute;
    margin: 0;
    color: var(--ink);
    font-size: 29px;
    font-weight: 400;
    line-height: 35px;
    letter-spacing: .5px;
    text-transform: uppercase;
  }
  .item-list {
    position: absolute;
    margin: 0;
    padding: 0;
    list-style: none;
    font-size: 35px;
    line-height: 39.5px;
  }
  .item-list li { position: relative; padding-left: 29px; }
  .item-list li::before {
    content: "";
    position: absolute;
    left: 0;
    top: 13px;
    width: 13px;
    height: 13px;
    border: 1.5px solid currentColor;
    box-sizing: border-box;
  }
  .deny-list { left: 79px; top: 236px; color: var(--deny-red); }
  .deny-list li::after {
    content: "×";
    position: absolute;
    left: 1px;
    top: 3px;
    font-size: 18px;
    line-height: 18px;
    font-weight: 700;
  }
  .allow-list { left: 569px; top: 236px; color: var(--allow-green); }
  .allow-list li::after {
    content: "✓";
    position: absolute;
    left: 2px;
    top: 4px;
    font-size: 13px;
    line-height: 16px;
  }
  .allow-list li.continued::before, .allow-list li.continued::after { display: none; }
  .divider {
    position: absolute;
    left: 495px;
    top: 181px;
    width: 5px;
    height: 391px;
    background: var(--brand-blue);
  }
  .fine-print {
    position: absolute;
    left: 38px;
    top: 590px;
    margin: 0;
    color: var(--ink);
    font-size: 27px;
    font-style: italic;
  }
  .thanks {
    position: absolute;
    left: 745px;
    top: 593px;
    width: 230px;
    margin: 0;
    text-align: center;
    color: var(--card-white);
    font-size: 25px;
    font-weight: 900;
    letter-spacing: 3px;
  }
</style>
</head>
<body>
  <section class="card" aria-label="Medical dietary restriction card">
    <div class="emblem-area" role="img" aria-label="Faint medical emblem decoration"></div>
    <svg class="bands" width="1000" height="640" viewBox="0 0 1000 640" aria-hidden="true">
      <polygon points="0,0 654,0 592,136 0,136" fill="var(--brand-blue)"/>
      <polygon points="735,583 1000,583 1000,640 711,640" fill="var(--brand-blue)"/>
    </svg>

    <header>
      <p class="title-kicker">MEDICAL</p>
      <h1 class="title-main">DIETARY RESTRICTION</h1>
    </header>

    <svg class="status-icon" style="left:46px;top:154px" viewBox="0 0 66 66" aria-hidden="true">
      <circle cx="33" cy="33" r="32" fill="var(--deny-red)"/>
      <path d="M21 21 L45 45 M45 21 L21 45" stroke="#fff" stroke-width="8" stroke-linecap="round"/>
    </svg>
    <h2 class="col-heading" style="left:125px;top:152px">I cannot eat<br>processed seed oils</h2>
    <ul class="item-list deny-list">
      <li>Vegetable oil</li>
      <li>Canola oil</li>
      <li>Soybean oil</li>
      <li>Sunflower oil</li>
      <li>Corn oil</li>
      <li>Cottonseed oil</li>
      <li>Safflower oil</li>
      <li>Peanut oil</li>
      <li>Sesame oil</li>
    </ul>

    <div class="divider"></div>

    <svg class="status-icon" style="left:535px;top:154px" viewBox="0 0 66 66" aria-hidden="true">
      <circle cx="33" cy="33" r="32" fill="var(--allow-green)"/>
      <path d="M18 34 L29 45 L49 22" stroke="#fff" stroke-width="8" fill="none" stroke-linecap="round" stroke-linejoin="round"/>
    </svg>
    <h2 class="col-heading" style="left:616px;top:152px">Natural oils &amp; fats<br>are acceptable</h2>
    <ul class="item-list allow-list">
      <li>Butter</li>
      <li>Extra virgin</li>
      <li class="continued">olive oil</li>
      <li>Avocado oil</li>
      <li>Coconut oil</li>
      <li>Ghee</li>
      <li>Lard</li>
      <li>Natural animal</li>
      <li class="continued">fats</li>
    </ul>

    <p class="fine-print">*Trace amounts acceptable. Reuse cookwares acceptable</p>
    <p class="thanks">THANK YOU</p>
  </section>
</body>
</html>
```